Corvalith is a financial services company which transacts by allowing clients to purchase Plinkmark (c

I need a ravo themed site (if possible) but I can work with html as well since I have paid for the CSS very simple that will simply show what corvalith is and what we graphically need to do in order to make the transaction happen

Target Market(s)

Any persons over the age of 18 globally who wants to purchase Plinkmark (crypto currency) with their credit cards and receive a plink wallet from Corvalith

Industry/Entity Type

Insurance

Coding

Coded - Design and coding required

Number of Pages Required

3 page

Font styles to use
Serif

Colors
3277b5
3176b5
85acd3
85cae6

Requirements
Must have
• Logo visible top let on all pages ... color scheme that evokes trust, confidence, transparency.. terms and conditions and privacy policy footer links
Nice to have
• I willl have logo chosen in next 24 hrs..

```html
<!DOCTYPE html>
<html lang="en">
<head>
<meta charset="utf-8">
<title>Corvalith – From Credit Card to Plinkmark in Seconds</title>
<link href="https://fonts.googleapis.com/css2?family=Open+Sans:wght@400;600&family=Roboto+Condensed:wght@400;700&display=swap" rel="stylesheet">
<style>
:root{
  --brand:#2f6fae;
  --ink:#222222;
  --muted:#555555;
  --white:#ffffff;
  --services:#0d63a2;
  --services-deep:#0a5590;
  --accent:#1e8fd0;
  --testi:#5cb8e2;
  --card-border:#1d3a66;
  --footer-text:#444444;
  --rule:#e3e3e3;
}
*{box-sizing:border-box;margin:0;padding:0}
html,body{width:1200px;height:2432px;overflow:hidden}
body{position:relative;background:var(--white);font-family:"Open Sans",sans-serif;color:var(--ink)}
.abs{position:absolute}
.heading{font-family:"Roboto Condensed",sans-serif;font-weight:400}

/* header */
.site-header{position:absolute;left:0;top:0;width:1200px;height:106px;background:var(--white)}
.logo{position:absolute;font-family:"Roboto Condensed",sans-serif;font-weight:700;color:var(--brand);letter-spacing:.5px}
.site-header .logo{left:89px;top:32px;font-size:36px;line-height:42px}
.main-nav a{position:absolute;top:43px;font-size:20px;color:var(--ink);text-decoration:none;line-height:24px}

/* hero */
.hero{position:absolute;left:0;top:106px;width:1200px;height:486px}
.hero-photo{position:absolute;inset:0;background:linear-gradient(120deg,#c9ced3 0%,#a9b0b8 35%,#6e757d 62%,#34393f 100%)}
.hero-title{position:absolute;left:0;width:1200px;top:180px;text-align:center;color:var(--white);font-size:39px;line-height:46px}
.hero-sub{position:absolute;left:0;width:1200px;top:242px;text-align:center;color:var(--white);font-size:24px;line-height:30px}
.slider-arrows{position:absolute;left:1061px;top:422px}

/* services */
.services{position:absolute;left:0;top:592px;width:1200px;height:498px;background:linear-gradient(180deg,var(--services) 0%,var(--services-deep) 100%);color:var(--white)}
.services h2{position:absolute;left:0;width:1200px;top:68px;text-align:center;font-size:36px;line-height:42px}
.services .intro{position:absolute;left:0;width:1200px;top:124px;text-align:center;font-size:15.5px;line-height:26px}
.service{position:absolute;top:222px;width:300px;text-align:center}
.service-icon{width:114px;height:114px;border-radius:50%;background:var(--white);margin:0 auto;display:flex;align-items:center;justify-content:center}
.service p{margin-top:26px;font-size:16px;line-height:23px}
.service p.cta{margin-top:37px;text-transform:uppercase}

/* why */
.why h2{position:absolute;left:199px;top:1218px;font-size:33px;line-height:40px;color:#111}
.why-list{position:absolute;left:199px;top:1264px;list-style:none}
.why-list li{font-size:14.5px;line-height:32px;color:#333;display:flex;align-items:center}
.why-list svg{margin-right:10px}
.btn{position:absolute;left:199px;top:1436px;width:138px;height:34px;background:var(--accent);color:var(--white);font-size:14.5px;line-height:34px;text-align:center;border-radius:2px}
.video{position:absolute;left:551px;top:1208px;width:472px;height:281px;background:#000}
.video-still{position:absolute;left:0;top:24px;width:472px;height:230px;background:linear-gradient(135deg,#8fb3c6 0%,#6c8fa5 40%,#445f7a 100%)}
.video-bar{position:absolute;left:0;bottom:0;width:472px;height:27px;background:#1a1a1a}

/* testimonials */
.testimonials{position:absolute;left:0;top:1584px;width:1200px;height:508px;background:var(--testi)}
.testimonials h2{position:absolute;left:0;width:1200px;top:66px;text-align:center;color:var(--white);font-size:32px;line-height:40px}
.testi-card{position:absolute;top:232px;width:285px;height:191px;background:var(--white);border:2px solid var(--card-border);box-shadow:0 4px 10px rgba(0,0,0,.18);text-align:center;padding:0 24px}
.avatar{position:absolute;left:82px;top:-98px;width:121px;height:121px;border-radius:50%;border:4px solid #d7dde3;background:linear-gradient(180deg,#e5e8eb,#aeb6bf)}
.testi-card .quote{margin-top:68px;font-size:14px;line-height:21px;color:#333}
.testi-card .name{margin-top:14px;font-size:19px;color:#222}

/* footer */
.site-footer .logo{left:136px;top:2208px;font-size:34px;line-height:40px}
.social{position:absolute;top:2260px;width:30px;height:30px;border-radius:50%}
.footer-col{position:absolute;top:2169px}
.footer-col h3{font-family:"Open Sans",sans-serif;font-weight:400;font-size:17px;color:#333;text-transform:uppercase;margin-bottom:14px}
.footer-col ul{list-style:none}
.footer-col li{font-size:13.5px;line-height:27px;color:var(--footer-text)}
.footer-col li::before{content:"»";margin-right:8px}
.contact-col li::before{content:none}
.contact-col li{display:flex;align-items:flex-start;line-height:24px;margin-bottom:8px}
.contact-col svg{flex:none;margin:4px 14px 0 0}
.rule{position:absolute;left:65px;top:2369px;width:1070px;height:1px;background:var(--rule)}
.copyright{position:absolute;left:0;width:1200px;top:2396px;text-align:center;font-size:12.5px;color:#333}
</style>
</head>
<body>

<header class="site-header">
  <div class="logo">Corvalith</div>
  <nav class="main-nav">
    <a style="left:634px">Home</a>
    <a style="left:754px">About Us</a>
    <a style="left:898px">FAQs</a>
    <a style="left:1009px">Support</a>
  </nav>
</header>

<section class="hero">
  <div class="hero-photo" role="img" aria-label="Business person working with a laptop, calculator and financial charts on a desk"></div>
  <h1 class="hero-title heading">From Credit Card to Plinkmark in Seconds</h1>
  <p class="hero-sub heading">Simple, Trusted, Low Fee Digital Money Platform</p>
  <svg class="slider-arrows" width="46" height="22" viewBox="0 0 46 22">
    <circle cx="10" cy="11" r="10" fill="#555"/><path d="M12 6 L7 11 L12 16" stroke="#fff" stroke-width="2" fill="none"/>
    <circle cx="35" cy="11" r="10" fill="#555"/><path d="M33 6 L38 11 L33 16" stroke="#fff" stroke-width="2" fill="none"/>
  </svg>
</section>

<section class="services">
  <h2 class="heading">OUR SERVICES</h2>
  <p class="intro">It is a long established fact that a reader will be distracted by the readable content of a page when looking at its layout.<br>The point of using Lorem Ipsum is that it has a more-or-less normal distribution of letters, as opposed</p>

  <div class="service" style="left:41px">
    <div class="service-icon">
      <svg width="52" height="52" viewBox="0 0 52 52" fill="none" stroke="#111" stroke-width="2.4"><circle cx="26" cy="26" r="22"/><circle cx="26" cy="26" r="16"/></svg>
    </div>
    <p>instantely exchange<br>your dollars for plinkmark</p>
  </div>
  <div class="service" style="left:310px">
    <div class="service-icon">
      <svg width="54" height="46" viewBox="0 0 54 46" fill="none" stroke="#111" stroke-width="2.4"><path d="M6 8 H42 V14"/><rect x="3" y="14" width="46" height="29" rx="3"/><rect x="34" y="23" width="17" height="11" rx="2"/><circle cx="40" cy="28.5" r="1.8" fill="#111"/></svg>
    </div>
    <p>Real time refunds receipt,<br>you get your own digital</p>
  </div>
  <div class="service" style="left:580px">
    <div class="service-icon">
      <svg width="56" height="56" viewBox="0 0 56 56" fill="none" stroke="#111" stroke-width="2.4"><circle cx="28" cy="28" r="24"/><path d="M12 14 C20 18 18 24 24 26 C30 28 26 36 30 42"/><path d="M36 8 C34 14 40 16 44 18 C48 22 44 28 50 30"/><path d="M14 36 C18 34 20 40 18 46"/></svg>
    </div>
    <p>Global freedom to push Plink<br>to whereever you want.</p>
  </div>
  <div class="service" style="left:855px">
    <div class="service-icon">
      <svg width="56" height="50" viewBox="0 0 56 50" fill="none" stroke="#111" stroke-width="2.4"><path d="M18 18 L26 4 M38 18 L30 4"/><rect x="3" y="18" width="50" height="6"/><path d="M7 24 L11 46 H45 L49 24"/><path d="M17 28 V42 M24 28 V42 M32 28 V42 M39 28 V42"/></svg>
    </div>
    <p class="cta">Click here to purchase</p>
  </div>
</section>

<section class="why">
  <h2 class="heading">WHY PLINKMARK?</h2>
  <ul class="why-list">
    <li><svg width="12" height="12" viewBox="0 0 12 12"><circle cx="6" cy="6" r="6" fill="#1a5d95"/><path d="M5 3.5 L7.5 6 L5 8.5" stroke="#fff" stroke-width="1.6" fill="none"/></svg>Easily transactable</li>
    <li><svg width="12" height="12" viewBox="0 0 12 12"><circle cx="6" cy="6" r="6" fill="#1a5d95"/><path d="M5 3.5 L7.5 6 L5 8.5" stroke="#fff" stroke-width="1.6" fill="none"/></svg>Great upside value proposition</li>
    <li><svg width="12" height="12" viewBox="0 0 12 12"><circle cx="6" cy="6" r="6" fill="#1a5d95"/><path d="M5 3.5 L7.5 6 L5 8.5" stroke="#fff" stroke-width="1.6" fill="none"/></svg>Super low transaction speed</li>
    <li><svg width="12" height="12" viewBox="0 0 12 12"><circle cx="6" cy="6" r="6" fill="#1a5d95"/><path d="M5 3.5 L7.5 6 L5 8.5" stroke="#fff" stroke-width="1.6" fill="none"/></svg>Revolution tranaction payout system</li>
    <li><svg width="12" height="12" viewBox="0 0 12 12"><circle cx="6" cy="6" r="6" fill="#1a5d95"/><path d="M5 3.5 L7.5 6 L5 8.5" stroke="#fff" stroke-width="1.6" fill="none"/></svg>Master nodes</li>
  </ul>
  <div class="btn">Push for Salmon</div>

  <div class="video">
    <div class="video-still" role="img" aria-label="Video still of three colleagues working together at a laptop in a bright office"></div>
    <svg class="abs" style="left:201px;top:114px" width="72" height="50" viewBox="0 0 72 50"><rect width="72" height="50" rx="11" fill="#1f1f1f" fill-opacity=".85"/><path d="M29 15 L47 25 L29 35 Z" fill="#fff"/></svg>
    <div class="video-bar">
      <svg class="abs" style="left:12px;top:7px" width="14" height="14" viewBox="0 0 14 14"><path d="M2 1 L13 7 L2 13 Z" fill="#ccc"/></svg>
      <svg class="abs" style="left:54px;top:8px" width="14" height="12" viewBox="0 0 14 12"><path d="M1 4 H4 L8 1 V11 L4 8 H1 Z" fill="#ccc"/></svg>
    </div>
  </div>
</section>

<section class="testimonials">
  <h2 class="heading">TESTIMONIALS</h2>
  <article class="testi-card" style="left:131px">
    <div class="avatar" role="img" aria-label="Portrait of Steve"></div>
    <p class="quote">I was able to use my card to buy cash in minutes, so happy</p>
    <p class="name">Steve</p>
  </article>
  <article class="testi-card" style="left:454px">
    <div class="avatar" role="img" aria-label="Portrait of Laura"></div>
    <p class="quote">The site is so easy, free sign up, enter card with how much Plink you want,</p>
    <p class="name">Laura</p>
  </article>
  <article class="testi-card" style="left:777px">
    <div class="avatar" role="img" aria-label="Portrait of Matt"></div>
    <p class="quote">As a newbie to crypto I was able to purchase my plinkmark with my credicard,, so easy!</p>
    <p class="name">Matt</p>
  </article>
</section>

<footer class="site-footer">
  <div class="logo abs">Corvalith</div>
  <span class="social" style="left:159px;background:#3b5998" aria-label="Social profile"></span>
  <span class="social" style="left:198px;background:#dc4a38" aria-label="Social profile"></span>
  <span class="social" style="left:239px;background:#3fa9e8" aria-label="Social profile"></span>

  <div class="footer-col" style="left:415px">
    <h3>Quick Links</h3>
    <ul><li>Privacy Policy</li><li>Login</li><li>Advanced Search</li><li>Contact Us</li></ul>
  </div>
  <div class="footer-col" style="left:668px">
    <h3>Links</h3>
    <ul><li>About</li><li>Products</li><li>Blog</li><li>Services</li></ul>
  </div>
  <div class="footer-col contact-col" style="left:881px">
    <h3>Contact Us</h3>
    <ul>
      <li><svg width="12" height="16" viewBox="0 0 12 16"><path d="M6 0 C2.7 0 0 2.6 0 5.8 C0 10 6 16 6 16 C6 16 12 10 12 5.8 C12 2.6 9.3 0 6 0 Z" fill="#1d3f72"/><circle cx="6" cy="5.8" r="2.2" fill="#fff"/></svg><span>P.O. Box 4410<br>Harlow Ridge, CT 06120</span></li>
      <li><svg width="14" height="14" viewBox="0 0 14 14"><path d="M3 0 L5.5 3.5 L4 5.5 C5 7.5 6.5 9 8.5 10 L10.5 8.5 L14 11 L12 14 C6 13.5 0.5 8 0 2 Z" fill="#1d3f72"/></svg><span>(888) 555-0147</span></li>
      <li><svg width="16" height="12" viewBox="0 0 16 12"><rect width="16" height="12" rx="1" fill="#1d3f72"/><path d="M1 1.5 L8 7 L15 1.5" stroke="#fff" stroke-width="1.4" fill="none"/></svg><span>info@corvalith.com</span></li>
    </ul>
  </div>

  <div class="rule"></div>
  <p class="copyright">Copyright © 2018&nbsp; All Rights Reserved</p>
</footer>

</body>
</html>
```